The Brightwater Compass Business Card

We need an attractive business card with the logo that we bought from ArtVantly last year.
Our mission is to contribute to change the way today's leaders manage business companies bringing value to the workplace and helping them to build a new model of creating wealth.
Our logo is clear about our values : we seek Positive Change through People and are convinced that the pursuit of individual well-being and the chase of economic results can converge with the right management.
Management Consulting
Corinne Fabrelle
+34 612 98 70 31
corinne.fabrelle@thebrightwatercompass-mail.net
www.thebrightwatercompass-mail.net

```html
<!DOCTYPE html>
<html lang="en">
<head>
<meta charset="utf-8">
<title>The Brightwater Compass – Business Card</title>
<link rel="stylesheet" href="https://fonts.googleapis.com/css2?family=Marcellus&family=Fira+Sans+Condensed:wght@300;400&display=swap">
<style>
  :root {
    --teal: #1f8079;
    --teal-dark: #17706a;
    --paper: #ffffff;
    --backdrop: #e6e6e8;
    --ink-light: #ffffff;
  }
  * { margin: 0; padding: 0; box-sizing: border-box; }
  html, body { width: 1200px; height: 1200px; overflow: hidden; }
  body {
    background: var(--backdrop);
    display: flex;
    flex-direction: column;
    align-items: center;
    justify-content: center;
    gap: 70px;
  }
  .card {
    position: relative;
    width: 760px;
    height: 434px;
    background: var(--paper);
    box-shadow: 0 2px 10px rgba(0,0,0,0.12);
    overflow: hidden;
  }

  /* Front */
  .front .wordmark {
    position: absolute;
    left: 0; right: 0;
    top: 78px;
    text-align: center;
    font-family: "Marcellus", serif;
    color: var(--teal);
  }
  .front .wordmark .brand-name {
    font-size: 44px;
    letter-spacing: 1px;
    text-transform: uppercase;
  }
  .front .wordmark .brand-line {
    margin-top: 10px;
    font-size: 16px;
    letter-spacing: 9px;
    text-transform: uppercase;
  }
  .band-rule {
    position: absolute;
    left: 0; right: 0;
    height: 2px;
    background: var(--teal);
  }
  .band-rule.upper { top: 236px; }
  .band-rule.lower { top: 386px; }
  .contact-band {
    position: absolute;
    left: 0; right: 0;
    top: 244px;
    height: 136px;
    background: var(--teal);
    display: flex;
    align-items: center;
    color: var(--ink-light);
    font-family: "Fira Sans Condensed", sans-serif;
  }
  .contact-band .person {
    width: 300px;
    text-align: center;
    font-size: 26px;
    font-weight: 400;
    letter-spacing: 0.5px;
    text-transform: uppercase;
  }
  .contact-band .divider {
    width: 1px;
    height: 92px;
    background: rgba(255,255,255,0.75);
  }
  .contact-band .details {
    list-style: none;
    padding-left: 24px;
    font-size: 17px;
    font-weight: 300;
    line-height: 1.6;
  }
  .contact-band .details li { display: flex; align-items: center; gap: 10px; }
  .contact-band .details svg { width: 15px; height: 15px; flex: none; }

  /* Back */
  .back {
    display: flex;
    align-items: center;
    justify-content: center;
    gap: 22px;
  }
  .back .brand-mark {
    width: 40px; height: 40px;
    border-radius: 50%;
    background: var(--teal);
  }
  .back .brand-name {
    font-family: "Marcellus", serif;
    font-size: 38px;
    color: var(--teal);
    text-transform: uppercase;
    letter-spacing: 1px;
  }
</style>
</head>
<body>

<section class="card front" aria-label="Business card front">
  <div class="wordmark">
    <div class="brand-name">The Brightwater</div>
    <div class="brand-line">Compass</div>
  </div>
  <div class="band-rule upper"></div>
  <div class="contact-band">
    <div class="person">Corinne Fabrelle</div>
    <div class="divider"></div>
    <ul class="details">
      <li>
        <svg viewBox="0 0 16 16" aria-hidden="true"><path fill="#fff" d="M3 1.5l2.5-.5 1.5 3.5-1.6 1.2a8 8 0 0 0 4.9 4.9l1.2-1.6 3.5 1.5-.5 2.5c-.2.7-.8 1-1.5 1C6.5 14 2 9.5 2 3c0-.7.3-1.3 1-1.5z"/></svg>
        +34 612 98 70 31
      </li>
      <li>
        <svg viewBox="0 0 16 16" aria-hidden="true"><circle cx="8" cy="8" r="6.5" fill="none" stroke="#fff" stroke-width="1.4"/><path d="M1.5 8h13M8 1.5c-3 3.5-3 9.5 0 13M8 1.5c3 3.5 3 9.5 0 13" fill="none" stroke="#fff" stroke-width="1.1"/></svg>
        www.thebrightwatercompass-mail.net
      </li>
      <li>
        <svg viewBox="0 0 16 16" aria-hidden="true"><rect x="1.5" y="3.5" width="13" height="9" fill="none" stroke="#fff" stroke-width="1.3"/><path d="M1.5 3.5L8 9l6.5-5.5" fill="none" stroke="#fff" stroke-width="1.3"/></svg>
        corinne.fabrelle@thebrightwatercompass-mail.net
      </li>
    </ul>
  </div>
  <div class="band-rule lower"></div>
</section>

<section class="card back" aria-label="Business card back">
  <div class="brand-mark"></div>
  <div class="brand-name">The Brightwater Compass</div>
</section>

</body>
</html>
```